**** Web design project for BoltNet ****

For my ICT company BoltNet I need a website.

We design, build and host web-applications and we have our own CMS product. In the references part we want to show sample websites (thumbnails) + links.

It should look modern (WEB 2.0), rounded corners.

I want the following menu' s:
- Home
- Services
- References
- News
- About BoltNet
- Contact

Sample websites:
See attachments
http://www.vandoqa.com
http://www.greyfoxmanagement.nl

Reason: Want to take some time for feedback and improvements.

Reason: I'm waiting for a black background, with shadow and ambient light. You'll make a good chance!

Industry/Entity Type

It Company

Requirements
Must have
• - Fixed width (1024px), should fit on an IPad2
- Language selection English/Dutch
- Twitter/Facebook/LinkedIn/RSS icons
- Footer for Terms of use and Copyrights
- Search box
- 3 (or more) boxes for information i.e. news, blog or advertisements
Nice to have
• - Footer Site Map
- Contrasting background outside borders
- wide image (rotator) (with transperant sentence block)
- Shadow

```html
<!DOCTYPE html>
<html lang="en">
<head>
<meta charset="utf-8">
<title>BoltNet</title>
<link rel="stylesheet" href="https://fonts.googleapis.com/css2?family=Montserrat:wght@300;400&family=Open+Sans:ital,wght@0,400;0,600;1,400&family=Cinzel:wght@400;700&display=swap">
<style>
:root{
  --black:#000;
  --orange:#f07a1e;
  --orange-dark:#d4691c;
  --orange-light:#e88c34;
  --page:#efefef;
  --navy:#1b3f66;
  --link:#1f7bc8;
  --text:#555;
  --steel:#8fa6b8;
  --bar:#dcdcdc;
}
*{margin:0;padding:0;box-sizing:border-box}
html,body{width:949px;height:1200px;overflow:hidden}
body{position:relative;background:var(--page);font-family:"Open Sans",Arial,sans-serif;color:var(--text)}
.abs{position:absolute}

/* header */
.header{position:absolute;left:0;top:0;width:949px;height:458px;background:radial-gradient(ellipse at 170px 60px,#0b1a2e 0,#000 170px)}
.topbar{left:600px;top:0;width:240px;height:25px;background:#e9e9e9;border-radius:0 0 22px 22px}
.search{left:612px;top:4px;width:116px;height:17px;background:#2a2a2a;color:#fff;font-size:8px;line-height:17px;padding-left:8px;font-family:Montserrat,sans-serif}
.search-btn{left:728px;top:4px;width:18px;height:17px;background:var(--orange)}
.flag{top:6px;width:17px;height:12px}
.logo-mark{left:113px;top:22px;width:70px;height:70px;border-radius:50%;background:#1f5f9a}
.logo-name{left:197px;top:32px;font-family:Montserrat,sans-serif;font-weight:300;font-size:34px;color:var(--steel)}
.nav{left:399px;top:46px;display:flex;gap:0;font-family:Montserrat,sans-serif;font-size:11.5px;color:#fff}
.nav a{color:#fff;text-decoration:none;padding:0 13px;line-height:20px}
.nav a.active{background:linear-gradient(#f4f4f4,#bdbdbd);color:#111;border-radius:5px;padding:0 12px;margin-right:2px}
.welcome{left:111px;top:139px;font-family:Montserrat,sans-serif;font-weight:300;font-size:23px;color:var(--orange)}
.intro{left:115px;top:182px;width:245px;font-size:11.4px;line-height:16.4px;color:#fff}
.learn{left:112px;top:371px;width:110px;height:35px;border-radius:18px;background:linear-gradient(#f98a2b,#d95a0a);border:2px solid #b8500e;color:#fff;font-family:Montserrat,sans-serif;font-size:14px;line-height:31px;text-align:center}
.slide{background:linear-gradient(#f3f3f3,#c22 30%,#e8e8e8 50%,#cfcfcf)}
.slider-line{left:0;top:440px;width:949px;height:2px;background:#555}
.slider-tab{left:412px;top:425px;width:124px;height:33px;background:#efefef;border:2px solid #555;border-bottom:none;border-radius:20px 20px 0 0}
.dot{top:433px;width:12px;height:12px;border-radius:50%;background:#fff;border:1px solid #999}
.dot.on{background:#d8231f}

/* content */
.heading{font-family:Cinzel,serif;font-size:16px;color:#555;letter-spacing:.5px}
.heading b{color:var(--navy)}
.rule{height:1px;background:#d0d0d0}
.lead{left:111px;top:506px;width:470px;font-size:9.6px;line-height:14px}
.tablet{left:113px;top:558px;width:190px;height:148px;border-radius:9px;background:#111;border:1px solid #555}
.tablet-screen{left:127px;top:572px;width:158px;height:118px;background:linear-gradient(#fafafa,#e6e6e6)}
.checks{left:323px;top:560px;list-style:none;font-size:9.8px;line-height:17.8px}
.checks li{display:flex;align-items:center;gap:8px}
.more-bar{height:18px;background:var(--bar);border-radius:4px;font-size:9px;line-height:18px;text-align:right;padding-right:8px;color:#666}
.news{left:649px;width:190px}
.news-thumb{width:53px;height:53px;border:1px solid #ccc;background:linear-gradient(#dfe5ea,#8a96a4)}
.news-title{left:65px;top:-3px;font-size:10.5px;color:var(--link)}
.news-text{left:65px;top:9px;width:125px;font-size:10px;line-height:12.6px}
.news-more{left:65px;top:43px;font-size:9px;font-style:italic}
.arrow{top:764px;font-size:14px;color:#555}
.customer{top:799px;width:131px;height:131px;border-radius:4px;background:linear-gradient(#c8202a 0,#c8202a 18%,#e9eef2 20%,#dadada 80%);box-shadow:0 3px 4px #bbb;border:2px solid #ddd}
.customer span{position:absolute;left:2px;right:2px;bottom:2px;height:18px;background:#333;color:#fff;font-size:10px;line-height:18px;text-align:center}

/* footer */
.footer{left:0;top:980px;width:949px;height:175px;background:linear-gradient(#e88a30,#d66c1e)}
.fhead{top:998px;font-family:Cinzel,serif;font-weight:700;font-size:11.5px;color:#fff}
.fsep{top:997px;width:1px;height:145px;background:#c6611a}
.field{left:111px;width:170px;height:21px;border-radius:6px;background:#fff;font-size:9.5px;color:#777;line-height:21px;padding-left:8px}
.subscribe{left:200px;top:1100px;width:82px;height:23px;border-radius:7px;background:linear-gradient(#ffd04a,#f29a12);border:1px solid #b86a0d;font-size:10.5px;color:#4a2a00;text-align:center;line-height:21px;font-family:Montserrat,sans-serif}
.flist{list-style:none;font-size:9.6px;line-height:16.3px;color:#fff}
.blog-date{font-size:9.6px;font-style:italic;color:#fff}
.blog-text{width:190px;font-size:9.6px;line-height:16px;color:#fff}
.bottom{left:0;top:1155px;width:949px;height:45px;background:#000}
.copyright{left:112px;top:1168px;font-size:9.5px;color:#fff}
.social{top:1162px;width:24px;height:24px;border-radius:50%;background:#e9e9e9}
</style>
</head>
<body>

<header class="header">
  <div class="abs topbar"></div>
  <div class="abs search">Enter your Keyword...</div>
  <div class="abs search-btn"></div>
  <svg class="abs flag" style="left:764px" viewBox="0 0 17 12" aria-label="English"><rect width="17" height="12" fill="#1f3f8a"/><path d="M0 0L17 12M17 0L0 12" stroke="#fff" stroke-width="2"/><path d="M8.5 0V12M0 6H17" stroke="#fff" stroke-width="3"/><path d="M8.5 0V12M0 6H17" stroke="#c8202a" stroke-width="1.5"/></svg>
  <svg class="abs flag" style="left:790px" viewBox="0 0 17 12" aria-label="Dutch"><rect width="17" height="4" fill="#c8202a"/><rect y="4" width="17" height="4" fill="#fff"/><rect y="8" width="17" height="4" fill="#1f3f8a"/></svg>

  <div class="abs logo-mark"></div>
  <div class="abs logo-name">BoltNet</div>

  <nav class="abs nav">
    <a class="active" href="#">Home</a><a href="#">Services</a><a href="#">References</a><a href="#">News</a><a href="#">About BoltNet</a><a href="#">Contact</a>
  </nav>

  <h1 class="abs welcome">Welcome to BoltNet</h1>
  <p class="abs intro">Contrary to popular belief, Lorem Ipsum is not simply random text. It has roots in a piece of classical Latin literature from 45 BC, making it over 2000 years old. Aldo Verhoef, a Latin professor at Marlow Ridge College in Virginia, looked up one of the more obscure Latin words, consectetur, from a Lorem Ipsum passage, and going through the cites of the word in classical literature, discovered the undoubtable source.</p>
  <div class="abs learn">LEARN MORE</div>

  <div class="abs slide" role="img" aria-label="Sample website screenshot" style="left:366px;top:230px;width:80px;height:115px"></div>
  <div class="abs slide" role="img" aria-label="Sample website screenshot" style="left:444px;top:200px;width:95px;height:150px"></div>
  <div class="abs slide" role="img" aria-label="Sample website screenshot with business people" style="left:536px;top:148px;width:302px;height:215px"></div>

  <div class="abs slider-line"></div>
  <div class="abs slider-tab"></div>
  <div class="abs dot on" style="left:428px"></div>
  <div class="abs dot" style="left:448px"></div>
  <div class="abs dot" style="left:468px"></div>
  <div class="abs dot" style="left:487px"></div>
  <div class="abs dot" style="left:507px"></div>
</header>

<section>
  <h2 class="abs heading" style="left:111px;top:474px">WHY <b>OUR CMS ?</b></h2>
  <div class="abs rule" style="left:111px;top:497px;width:479px"></div>
  <p class="abs lead">Lorem ipsum dolor sit amet, consectetur adipisicing elit, sed do eiusmod tempor incididunt ut labore et dolore magna aliqua. veniam, quilamco laboris nisi ut aliquip ex ea commodo consequat :-</p>
  <div class="abs tablet"></div>
  <div class="abs tablet-screen" role="img" aria-label="CMS website shown on a tablet"></div>
  <ul class="abs checks">
    <li><svg width="11" height="11" viewBox="0 0 11 11"><rect x=".5" y="2.5" width="8" height="8" fill="none" stroke="#888"/><path d="M2 6l2.5 2.5L10 1" stroke="#444" stroke-width="1.6" fill="none"/></svg>Vivamus sit amet tellus ut metus blandit sapien.</li>
    <li><svg width="11" height="11" viewBox="0 0 11 11"><rect x=".5" y="2.5" width="8" height="8" fill="none" stroke="#888"/><path d="M2 6l2.5 2.5L10 1" stroke="#444" stroke-width="1.6" fill="none"/></svg>Proin in metus eu augue feugiat placerat &nbsp;odio.</li>
    <li><svg width="11" height="11" viewBox="0 0 11 11"><rect x=".5" y="2.5" width="8" height="8" fill="none" stroke="#888"/><path d="M2 6l2.5 2.5L10 1" stroke="#444" stroke-width="1.6" fill="none"/></svg>Quisque non orci id tortor blandit auctor amet.</li>
    <li><svg width="11" height="11" viewBox="0 0 11 11"><rect x=".5" y="2.5" width="8" height="8" fill="none" stroke="#888"/><path d="M2 6l2.5 2.5L10 1" stroke="#444" stroke-width="1.6" fill="none"/></svg>Vestibulum eleifend libero odio, eleifend viverra</li>
    <li><svg width="11" height="11" viewBox="0 0 11 11"><rect x=".5" y="2.5" width="8" height="8" fill="none" stroke="#888"/><path d="M2 6l2.5 2.5L10 1" stroke="#444" stroke-width="1.6" fill="none"/></svg>Proin pretium ligula ut massa pellentesque</li>
    <li><svg width="11" height="11" viewBox="0 0 11 11"><rect x=".5" y="2.5" width="8" height="8" fill="none" stroke="#888"/><path d="M2 6l2.5 2.5L10 1" stroke="#444" stroke-width="1.6" fill="none"/></svg>Aliquam mollis malesuada dolor, sed placerat</li>
    <li><svg width="11" height="11" viewBox="0 0 11 11"><rect x=".5" y="2.5" width="8" height="8" fill="none" stroke="#888"/><path d="M2 6l2.5 2.5L10 1" stroke="#444" stroke-width="1.6" fill="none"/></svg>Proin pretium ligula ut massa pellentesque</li>
    <li><svg width="11" height="11" viewBox="0 0 11 11"><rect x=".5" y="2.5" width="8" height="8" fill="none" stroke="#888"/><path d="M2 6l2.5 2.5L10 1" stroke="#444" stroke-width="1.6" fill="none"/></svg>Aliquam mollis malesuada dolor, sed placerat</li>
  </ul>
  <div class="abs more-bar" style="left:111px;top:724px;width:479px">Read More ›</div>

  <h2 class="abs heading" style="left:649px;top:474px">LATEST <b>NEWS</b></h2>
  <div class="abs rule" style="left:649px;top:497px;width:187px"></div>
  <div class="abs news" style="top:511px">
    <div class="news-thumb" role="img" aria-label="Photo of a cheering team"></div>
    <div class="abs news-title">Contrary to popular</div>
    <div class="abs news-text">Lorem Ipsum is not simply random text...</div>
    <div class="abs news-more">Read More...</div>
  </div>
  <div class="abs news" style="top:584px">
    <div class="news-thumb" role="img" aria-label="Photo of a cheering team"></div>
    <div class="abs news-title">Contrary to popular</div>
    <div class="abs news-text">Lorem Ipsum is not simply random text...</div>
    <div class="abs news-more">Read More...</div>
  </div>
  <div class="abs news" style="top:656px">
    <div class="news-thumb" role="img" aria-label="Photo of a cheering team"></div>
    <div class="abs news-title">Contrary to popular</div>
    <div class="abs news-text">Lorem Ipsum is not simply random text...</div>
    <div class="abs news-more">Read More...</div>
  </div>
  <div class="abs more-bar" style="left:649px;top:724px;width:187px">View All News ›</div>

  <h2 class="abs heading" style="left:111px;top:762px"><b>OUR CUSTOMERS</b></h2>
  <div class="abs arrow" style="left:809px">‹</div>
  <div class="abs arrow" style="left:827px">›</div>
  <div class="abs customer" style="left:111px" role="img" aria-label="Customer website thumbnail"><span>www.domainname.com</span></div>
  <div class="abs customer" style="left:260px" role="img" aria-label="Customer website thumbnail"><span>www.domainname.com</span></div>
  <div class="abs customer" style="left:409px" role="img" aria-label="Customer website thumbnail"><span>www.domainname.com</span></div>
  <div class="abs customer" style="left:557px" role="img" aria-label="Customer website thumbnail"><span>www.domainname.com</span></div>
  <div class="abs customer" style="left:705px" role="img" aria-label="Customer website thumbnail"><span>www.domainname.com</span></div>
</section>

<footer>
  <div class="abs footer"></div>
  <div class="abs fhead" style="left:111px">SUBSCRIBE OUR NEWSLETTER!</div>
  <div class="abs field" style="top:1033px">Enter Your Name</div>
  <div class="abs field" style="top:1063px">Enter Your Email Address</div>
  <div class="abs subscribe">SUBSCRIBE</div>
  <div class="abs fsep" style="left:315px"></div>

  <div class="abs fhead" style="left:343px">QUICK LINKS</div>
  <ul class="abs flist" style="left:343px;top:1028px"><li>Home</li><li>Services</li><li>References</li><li>News</li><li>About BoltNet</li><li>Contact</li></ul>
  <div class="abs fsep" style="left:448px"></div>

  <div class="abs fhead" style="left:477px">CONTACT US</div>
  <ul class="abs flist" style="left:477px;top:1028px"><li>Lorem ipsum dolor amet,</li><li>Consectetur adipiscing,</li><li>Contary popular,</li><li>Sit amet.</li><li>Ph - 123 456 7890</li><li>Fax - 123 456 7890</li></ul>
  <div class="abs fsep" style="left:618px"></div>

  <div class="abs fhead" style="left:647px">BLOG</div>
  <div class="abs blog-date" style="left:647px;top:1029px">12 April 2012</div>
  <div class="abs blog-text" style="left:647px;top:1045px">Lorem ipsum dolor sit amet, consectetur adipiscing elit ...</div>
  <div class="abs rule" style="left:647px;top:1086px;width:190px;background:#c6611a"></div>
  <div class="abs blog-date" style="left:647px;top:1094px">12 April 2012</div>
  <div class="abs blog-text" style="left:647px;top:1110px">Lorem ipsum dolor sit amet, consectetur adipiscing elit ...</div>

  <div class="abs bottom"></div>
  <div class="abs copyright">Copyright©2012 BoltNet. All Rights Reserved.</div>
  <div class="abs social" style="left:721px" aria-label="Social profile"></div>
  <div class="abs social" style="left:751px" aria-label="Social profile"></div>
  <div class="abs social" style="left:783px" aria-label="Social profile"></div>
  <div class="abs social" style="left:813px" aria-label="News feed"></div>
</footer>

</body>
</html>
```